Flyer für Mobile Massage am Arbeitsplatz
Zielgruppe
Der Flyer richtet sich an Geschäftsleitungen, Firmenvorstände, Betriebsräte.
Ich werde den Flyer sowohl persönlich überreichen, als auch postalisch verschicken.
Aufgabenstellung
Es geht um einen Flyer, DIN lang, Hochformat, beidseitig bedruckt.

```html
<!DOCTYPE html>
<html lang="de">
<head>
<meta charset="utf-8">
<title>Mobile Massage am Arbeitsplatz – Flyer</title>
<link rel="stylesheet" href="https://fonts.googleapis.com/css2?family=Arimo:wght@400;700&display=swap">
<style>
  :root {
    --bg: #ffffff;
    --paper: #ffffff;
    --gold: #c8b27c;
    --gold-dark: #b59a5c;
    --cream: #f3ecd8;
    --cream-light: #faf6ea;
    --photo-a: #8a7a64;
    --photo-b: #c9a64a;
    --photo-c: #6b5a4a;
    --ink: #111111;
  }
  * { box-sizing: border-box; margin: 0; padding: 0; }
  html, body { width: 1200px; height: 900px; overflow: hidden; background: var(--bg); }
  body { font-family: "Arimo", Arial, sans-serif; position: relative; }

  .panel {
    position: absolute;
    top: 57px;
    width: 463px;
    height: 716px;
    background: var(--paper);
    overflow: hidden;
    box-shadow: 0 0 0 1px #eee;
  }
  .panel--front { left: 112px; }
  .panel--back { left: 630px; }
  .panel__deco { position: absolute; inset: 0; width: 463px; height: 716px; }

  .title {
    position: absolute;
    left: 42px;
    top: 186px;
    color: var(--gold);
    font-size: 25px;
    font-weight: 400;
    letter-spacing: 5px;
    line-height: 35px;
  }
  .title__line--center { padding-left: 70px; }
  .contact {
    position: absolute;
    left: 42px;
    top: 344px;
    color: var(--gold);
    font-size: 12px;
    line-height: 18px;
  }

  .body-copy {
    position: absolute;
    left: 40px;
    top: 172px;
    width: 184px;
    font-size: 11px;
    line-height: 14.5px;
    color: var(--ink);
    text-align: justify;
  }
  .body-copy p + p { margin-top: 9px; }

  .tax-note {
    position: absolute;
    left: 30px;
    width: 403px;
    top: 518px;
    text-align: center;
    font-size: 13px;
    line-height: 18px;
    color: var(--ink);
  }
  .pricing {
    position: absolute;
    left: 0;
    width: 463px;
    top: 578px;
    text-align: center;
    font-size: 13px;
    line-height: 17px;
    color: var(--ink);
  }
  .pricing__head { font-size: 14px; }
</style>
</head>
<body>

<section class="panel panel--front">
  <svg class="panel__deco" viewBox="0 0 463 716" xmlns="http://www.w3.org/2000/svg">
    <defs>
      <linearGradient id="photoBandA" x1="0" y1="0" x2="1" y2="0">
        <stop offset="0" stop-color="var(--photo-c)"/>
        <stop offset="0.5" stop-color="var(--photo-a)"/>
        <stop offset="1" stop-color="var(--photo-b)"/>
      </linearGradient>
      <radialGradient id="photoRoundA" cx="0.5" cy="0.5" r="0.6">
        <stop offset="0" stop-color="var(--photo-b)"/>
        <stop offset="1" stop-color="var(--photo-c)"/>
      </radialGradient>
      <linearGradient id="creamFoot" x1="0" y1="0" x2="0" y2="1">
        <stop offset="0" stop-color="var(--cream)"/>
        <stop offset="1" stop-color="var(--cream-light)"/>
      </linearGradient>
    </defs>
    <path d="M0 0 H463 V8 Q250 40 0 150 Z" fill="url(#photoBandA)" role="img" aria-label="Foto: Massage am Arbeitsplatz auf Massagestühlen"/>
    <path d="M0 150 Q250 40 463 8 V24 Q260 62 0 172 Z" fill="var(--cream)"/>
    <path d="M0 150 Q250 40 463 8" fill="none" stroke="var(--gold)" stroke-width="1.5"/>

    <circle cx="405" cy="312" r="92" fill="var(--cream)"/>
    <circle cx="405" cy="312" r="82" fill="url(#photoRoundA)" role="img" aria-label="Foto: Nackenmassage auf einem Massagestuhl"/>
    <circle cx="378" cy="522" r="156" fill="var(--cream)"/>
    <circle cx="378" cy="522" r="143" fill="url(#photoRoundA)" role="img" aria-label="Foto: Handmassage im Büro"/>

    <path d="M0 648 Q230 700 463 636 V716 H0 Z" fill="url(#creamFoot)"/>
    <path d="M0 672 Q240 716 463 660" fill="none" stroke="var(--gold)" stroke-width="1.2" opacity="0.7"/>
  </svg>

  <h1 class="title">
    <span class="title__line">MobileMassage</span><br>
    <span class="title__line title__line--center">am</span><br>
    <span class="title__line">Arbeitsplatz</span>
  </h1>
  <p class="contact">
    Tel.: 030 - 55501234<br>
    www.mobile-massage-lindenhain.de
  </p>
</section>

<section class="panel panel--back">
  <svg class="panel__deco" viewBox="0 0 463 716" xmlns="http://www.w3.org/2000/svg">
    <defs>
      <linearGradient id="photoBandB" x1="0" y1="0" x2="1" y2="0">
        <stop offset="0" stop-color="var(--photo-c)"/>
        <stop offset="0.5" stop-color="var(--photo-a)"/>
        <stop offset="1" stop-color="var(--photo-b)"/>
      </linearGradient>
      <linearGradient id="photoPeople" x1="0" y1="0" x2="0" y2="1">
        <stop offset="0" stop-color="#9aa6b8"/>
        <stop offset="0.6" stop-color="#3a3f4a"/>
        <stop offset="1" stop-color="var(--photo-b)"/>
      </linearGradient>
      <linearGradient id="creamFootB" x1="0" y1="0" x2="0" y2="1">
        <stop offset="0" stop-color="var(--cream)"/>
        <stop offset="1" stop-color="var(--cream-light)"/>
      </linearGradient>
    </defs>
    <path d="M0 0 H463 V8 Q250 40 0 150 Z" fill="url(#photoBandB)" role="img" aria-label="Foto: Massage am Arbeitsplatz auf Massagestühlen"/>
    <path d="M0 150 Q250 40 463 8 V24 Q260 62 0 172 Z" fill="var(--cream)"/>
    <path d="M0 150 Q250 40 463 8" fill="none" stroke="var(--gold)" stroke-width="1.5"/>

    <rect x="256" y="186" width="158" height="250" rx="30" fill="url(#photoPeople)" role="img" aria-label="Freigestelltes Foto: Masseur behandelt einen Kunden auf dem Massagestuhl"/>

    <path d="M0 648 Q230 700 463 636 V716 H0 Z" fill="url(#creamFootB)"/>
    <path d="M0 672 Q240 716 463 660" fill="none" stroke="var(--gold)" stroke-width="1.2" opacity="0.7"/>
  </svg>

  <div class="body-copy">
    <p>In unseren Massagen am Arbeitsplatz lassen wir Elemente aus der Shiatsu - Energiemassage und der Joint Release - Gelenklockerungen zusammenfließen. Auf diese Weise eröffnen wir einen Raum für spürbare Entspannung mitten im Arbeitsalltag.</p>
    <p>Die Massagen befreien aus berufsbedingten Zwangshaltungen, wirken stresslindernd und stimmungshebend im team , fokussieren auf die Problemzonen im Büro: Rücken, Nacken, Schulter und Maushand und sind ein Baustein im innerbetrieblichen Gesundheitsmanagement.</p>
  </div>

  <p class="tax-note">Die Kosten können, sofern vom Arbeitgeber getragen, nach §3 Nr.34 EstG von der Steuer abgesetzt werden.</p>

  <div class="pricing">
    <p class="pricing__head">Preise:</p>
    <p>20 Minuten : 16 Euro</p>
    <p>inklusive Anfahrt</p>
    <p>buchbar ab 4 Personen</p>
  </div>
</section>

</body>
</html>
```